Letterhead for New Orthopaedic Surgery Practice

My husband and I are starting our own practice named RB Spine & Vitality Center. We would like to create a nice simple but high class letterhead that doesn't use too much solid color ink when printing. I like the colors dark blue, gold, yellow. Open to other suggestions. We will need to list him and I both on the top of the letterhead. Here is the important information:
Lucinda Perrow, M.D. - Hand and Upper Extremity Surgery
Abena Quist, M.D. - Hip & Knee Replacement/General Orthopaedic Surgery
Location: 18735 North Harlow Pkwy
Palm Ridge, FL 33490
Phone: 954-218-4650
Fax: 954-582-1346
Email: info@myrbspine.com

The only thing is that the phone and fax numbers will change once we get into our space. I just want to get the design started. I am including several documents which are my previous practice letterhead, my current procedure room letterhead, and our new Logo. The other letterheads are just for examples but please think outside of the box! We would love to see some great designs.

Colors
0054AA
0677BA
7BADD7
CADEEF
E8F1F8
0094D4
00A9DD
6FCCEA
C7EBF8
E9F6FB

Requirements
Must have
• class, elegance, luxury

```html
<!DOCTYPE html>
<html lang="en">
<head>
<meta charset="utf-8">
<title>RB Spine &amp; Vitality Center — Letterhead</title>
<link rel="stylesheet" href="https://fonts.googleapis.com/css2?family=Poppins:wght@400;500;600;700&display=swap">
<style>
  :root {
    --navy: #233a7d;
    --cyan: #1ab8e0;
    --rule: #1cb6df;
    --band-top: #213f86;
    --band-bottom: #2a9fd6;
    --foot-top: #1f699f;
    --foot-bottom: #1f90c0;
    --gold-light: #f7c21a;
    --gold-deep: #f0a021;
    --divider-gold: #e9b526;
    --page-bg: #f2f2f4;
    --paper: #ffffff;
    --watermark: #eeeef6;
  }
  * { box-sizing: border-box; margin: 0; padding: 0; }
  html, body {
    width: 1200px; height: 1200px; overflow: hidden;
    background: var(--page-bg);
    font-family: "Poppins", sans-serif;
  }
  .letterhead {
    position: absolute; left: 197px; top: 30px;
    width: 806px; height: 1140px;
    background: var(--paper);
    overflow: hidden;
  }
  .practice-title {
    position: absolute; left: 0; top: 50px; width: 580px;
    text-align: center; color: var(--navy);
    font-weight: 700; font-size: 44px; line-height: 46px;
  }
  .practice-title .accent { color: var(--cyan); }
  .brand-mark {
    position: absolute; left: 596px; top: 68px; width: 180px;
    display: flex; align-items: center; gap: 10px;
  }
  .brand-mark .dot {
    width: 34px; height: 34px; border-radius: 50%;
    background: var(--navy); flex: none;
  }
  .brand-mark .name {
    color: var(--navy); font-weight: 600; font-size: 14px; line-height: 17px;
  }
  .doctor-band {
    position: absolute; left: 0; top: 159px; width: 806px; height: 92px;
    background: linear-gradient(var(--band-top), var(--band-bottom));
    display: flex;
  }
  .doctor {
    width: 402px; text-align: center; color: #fff;
    display: flex; flex-direction: column; justify-content: flex-start;
    padding-top: 14px;
  }
  .doctor + .doctor { width: 404px; border-left: 4px solid var(--divider-gold); padding-top: 7px; }
  .doctor .name {
    font-weight: 700; font-size: 28px; line-height: 34px;
    background: linear-gradient(var(--gold-light), var(--gold-deep));
    -webkit-background-clip: text; background-clip: text; color: transparent;
  }
  .doctor .specialty { font-size: 16px; line-height: 20px; }
  .patient-row {
    position: absolute; left: 0; top: 275px; width: 806px; height: 47px;
    border-top: 2px solid var(--rule); border-bottom: 2px solid var(--rule);
    display: flex; color: var(--navy); font-weight: 700; font-size: 19px;
  }
  .patient-row .field { display: flex; align-items: center; }
  .field.patient { width: 445px; padding-left: 67px; padding-top: 4px; }
  .field.age { width: 124px; border-left: 2px solid var(--rule); padding-left: 15px; }
  .field.date { flex: 1; border-left: 2px solid var(--rule); padding-left: 16px; }
  .margin-rule {
    position: absolute; left: 237px; top: 322px; width: 2px; height: 709px;
    background: var(--rule);
  }
  .watermark {
    position: absolute; left: 0; top: 560px; width: 806px;
    text-align: center; color: var(--watermark);
    font-weight: 600; font-size: 52px; line-height: 64px;
  }
  .contact-footer {
    position: absolute; left: 0; top: 1031px; width: 806px; height: 109px;
    background: linear-gradient(var(--foot-top), var(--foot-bottom));
    color: #fff;
  }
  .contact-item { position: absolute; top: 16px; }
  .contact-item .label { font-weight: 600; font-size: 15px; line-height: 20px; }
  .contact-item .value { font-size: 16px; line-height: 24px; margin-top: 6px; }
  .contact-item.phone { left: 47px; }
  .contact-item.fax { left: 178px; }
  .contact-item.email { left: 321px; top: 19px; }
  .contact-item.email .value { font-size: 15px; margin-top: 3px; }
  .address {
    position: absolute; left: 526px; top: 20px; width: 240px;
    text-align: center; font-weight: 500; font-size: 16px; line-height: 21px;
  }
  .pin { position: absolute; left: 628px; top: -16px; }
</style>
</head>
<body>
  <main class="letterhead">
    <h1 class="practice-title">RB Spine &amp; <span class="accent">Vitality</span><br>Center</h1>

    <div class="brand-mark">
      <span class="dot"></span>
      <span class="name">RB Spine &amp; Vitality Center</span>
    </div>

    <section class="doctor-band">
      <div class="doctor">
        <div class="name">Lucinda Perrow, M.D.</div>
        <div class="specialty">Hand and Upper Extremity Surgery</div>
      </div>
      <div class="doctor">
        <div class="name">Abena Quist, M.D.</div>
        <div class="specialty">Hip &amp; Knee Replacement/General<br>Orthopaedic Surgery</div>
      </div>
    </section>

    <div class="patient-row">
      <div class="field patient">Patient Name</div>
      <div class="field age">Age</div>
      <div class="field date">Date</div>
    </div>

    <div class="margin-rule"></div>

    <div class="watermark" aria-hidden="true">RB Spine &amp; Vitality<br>Center</div>

    <footer class="contact-footer">
      <svg class="pin" width="32" height="32" viewBox="0 0 32 32" aria-hidden="true">
        <circle cx="16" cy="16" r="14" fill="var(--foot-top)" stroke="#fff" stroke-width="2.5"/>
        <path d="M16 8.5a5 5 0 0 0-5 5c0 3.8 5 9 5 9s5-5.2 5-9a5 5 0 0 0-5-5z" fill="#fff"/>
        <circle cx="16" cy="13.5" r="1.9" fill="var(--foot-top)"/>
      </svg>
      <div class="contact-item phone"><div class="label">Phone</div><div class="value">941-385-2074</div></div>
      <div class="contact-item fax"><div class="label">Fax</div><div class="value">954-582-1346</div></div>
      <div class="contact-item email"><div class="label">Email</div><div class="value">contact@myrbspine.com</div></div>
      <div class="address">18735 North Harlow Pkwy<br>Palm Ridge, FL 33490</div>
    </footer>
  </main>
</body>
</html>
```